" Empresa especializada em auditar e/ou prestar consultoria nos processos voltados para a área de supply chain. O trabalho desenvolvido é customizado de acordo com as necessidades de cada cliente. "

```html
<!DOCTYPE html>
<html lang="pt-BR">
<head>
<meta charset="utf-8">
<title>Vantis — Auditoria e Consultoria em Supply Chain</title>
<link href="https://fonts.googleapis.com/css2?family=Roboto:wght@400;500;700&display=swap" rel="stylesheet">
<style>
  :root {
    --brand-blue: #1fa3d6;
    --ink-grey: #6b6e72;
    --body-ink: #3d3f42;
    --paper: #ffffff;
    --backdrop: #e9ebed;
    --photo-dark: #b4b7bb;
    --photo-mid: #d6d8db;
    --photo-light: #f2f3f4;
  }
  * { margin: 0; padding: 0; box-sizing: border-box; }
  html, body {
    width: 1200px; height: 1200px; overflow: hidden;
    background: var(--backdrop);
    font-family: "Roboto", Arial, sans-serif;
  }
  .flyer {
    position: absolute; left: 197px; top: 30px;
    width: 806px; height: 1140px;
    background: var(--paper);
    overflow: hidden;
    box-shadow: 0 6px 24px rgba(0,0,0,.15);
  }
  .flyer-shapes { position: absolute; inset: 0; }
  .brand {
    position: absolute; right: 60px; top: 56px;
    display: flex; align-items: center; gap: 12px;
  }
  .brand-dot { width: 40px; height: 40px; border-radius: 50%; background: var(--brand-blue); flex: none; }
  .brand-name {
    font-weight: 700; font-size: 40px; letter-spacing: 2px; color: var(--brand-blue);
  }
  .headline {
    position: absolute; right: 60px; top: 130px;
    text-align: right; color: var(--ink-grey);
    font-weight: 700; font-size: 36px; line-height: 1.15;
  }
  .headline .accent { color: var(--brand-blue); }
  .about {
    position: absolute; left: 56px; top: 500px; width: 320px;
    color: var(--body-ink);
  }
  .about-title {
    color: var(--brand-blue); font-weight: 700; font-size: 30px; margin-bottom: 14px;
  }
  .about p { font-size: 14.5px; line-height: 1.45; margin-bottom: 14px; }
  .brand-mark-large {
    position: absolute; right: 50px; top: 780px;
    display: flex; align-items: center; gap: 14px;
  }
  .brand-mark-large .brand-dot { width: 60px; height: 60px; background: none; border: 4px solid var(--paper); }
  .brand-mark-large .brand-name { color: var(--paper); font-size: 40px; }
  .offer {
    position: absolute; left: 470px; top: 885px; width: 290px;
    color: var(--paper); font-size: 14.5px; line-height: 1.45;
  }
  .contact-bar {
    position: absolute; left: 0; right: 0; bottom: 0; height: 80px;
    display: flex; justify-content: space-around; align-items: center;
    padding: 0 40px; color: var(--ink-grey); font-size: 13px;
  }
  .contact-item { display: flex; align-items: center; gap: 8px; }
  .contact-item svg { width: 18px; height: 18px; fill: var(--brand-blue); flex: none; }
</style>
</head>
<body>
<main class="flyer">
  <svg class="flyer-shapes" viewBox="0 0 806 1140" width="806" height="1140">
    <defs>
      <linearGradient id="photoTone" x1="0" y1="0" x2="1" y2="0.3">
        <stop offset="0" stop-color="var(--photo-dark)"/>
        <stop offset="0.55" stop-color="var(--photo-mid)"/>
        <stop offset="1" stop-color="var(--photo-light)"/>
      </linearGradient>
    </defs>
    <polygon role="img" aria-label="Fotografia de arquitetura moderna em tons de cinza"
             points="0,240 806,180 806,400 0,760" fill="url(#photoTone)" opacity="0.8"/>
    <polygon points="0,240 390,210 0,520" fill="var(--paper)" opacity="0.55"/>
    <polygon class="blue-panel" points="806,400 806,1060 260,1060" fill="var(--brand-blue)"/>
    <polygon points="806,1060 806,1140 0,1140 0,1060" fill="var(--paper)"/>
  </svg>

  <div class="brand">
    <span class="brand-dot"></span>
    <span class="brand-name">VANTIS</span>
  </div>

  <h1 class="headline">Auditoria e Consultoria<br>voltada para a área<br>de <span class="accent">Supply Chain</span></h1>

  <section class="about">
    <h2 class="about-title">Quem Somos</h2>
    <p>Lorem ipsum dolor sit amet, consectetur adipiscing elit. Etiam ultrices dui sed pretium iaculis. Aliquam efficitur dui odio, eu congue augue auctor et. Donec a massa quis nisl ante.</p>
    <p>Vivamus diam velit, sollicitudin nec ultrices eu, dapibus sed augue ante. Aenean felis leo, cursus sit amet augue.</p>
    <p>Lorem ipsum dolor sit amet, consectetur adipiscing elit. Etiam ultrices dui sed pretium iaculis. Aliquam efficitur dui odio, eu congue augue auctor et. Donec a massa quis nisl ante.</p>
    <p>Vivamus diam velit, sollicitudin nec ultrices eu, dui sed augue ante. Aenean felis leo, cursus sollicitudin congue sit amet augue.</p>
  </section>

  <div class="brand-mark-large">
    <span class="brand-dot"></span>
    <span class="brand-name">VANTIS</span>
  </div>

  <p class="offer">Lorem ipsum dolor sit amet, consectetur adipiscing elit. Etiam ultrices dui sed pretium iaculis. Aliquam efficitur dui odio, eu congue augue auctor et. Donec a massa quis nisl ante.</p>

  <footer class="contact-bar">
    <div class="contact-item">
      <svg viewBox="0 0 24 24"><path d="M6.6 10.8a15 15 0 0 0 6.6 6.6l2.2-2.2a1 1 0 0 1 1-.25 11.4 11.4 0 0 0 3.6.57 1 1 0 0 1 1 1V20a1 1 0 0 1-1 1A17 17 0 0 1 3 4a1 1 0 0 1 1-1h3.5a1 1 0 0 1 1 1c0 1.25.2 2.45.57 3.57a1 1 0 0 1-.25 1z"/></svg>
      <span>(11) 4000-2200</span>
    </div>
    <div class="contact-item">
      <svg viewBox="0 0 24 24"><path d="M2 5h20v14H2zm2 2v.4l8 5 8-5V7zm16 2.8-8 5-8-5V17h16z"/></svg>
      <span>contato@vantis.com.br</span>
    </div>
    <div class="contact-item">
      <svg viewBox="0 0 24 24"><path d="M12 2a10 10 0 1 0 0 20 10 10 0 0 0 0-20zm0 2a8 8 0 0 1 0 16 8 8 0 0 1 0-16z"/></svg>
      <span>www.vantis.com.br</span>
    </div>
    <div class="contact-item">
      <svg viewBox="0 0 24 24"><path d="M12 2a7 7 0 0 0-7 7c0 5 7 13 7 13s7-8 7-13a7 7 0 0 0-7-7zm0 9.5A2.5 2.5 0 1 1 12 6.5a2.5 2.5 0 0 1 0 5z"/></svg>
      <span>Rua das Palmeiras, 120<br>São Paulo - SP</span>
    </div>
  </footer>
</main>
</body>
</html>
```